We need a design for the front page of our website

A redesign of our website front page.
www.brook-lantern.net. We are looking for a cleaner bolder fresher look with the confines of the website header as we are redesigning the whole site.

Industry/Entity Type

Tv

Number of Pages Required

1 page

Colors
ffc214

```html
<!DOCTYPE html>
<html lang="en">
<head>
<meta charset="utf-8">
<title>Brook Lantern – Home</title>
<link rel="stylesheet" href="https://fonts.googleapis.com/css2?family=Open+Sans:wght@400;600;700&family=Oswald:wght@400;500&family=Raleway:wght@300;400;500;600&display=swap">
<style>
:root{
  --orange:#e38a17;
  --orange-soft:#f6dfbd;
  --ink:#222;
  --text:#444;
  --muted:#8a8a8a;
  --line:#e3e3e3;
  --panel:#f7f7f7;
  --hero:#e9e7e7;
  --black:#0c0c0c;
  --fb:#1e74d0;
  --tw:#1da3e2;
  --li:#1c5878;
  --red:#d8262a;
}
*{box-sizing:border-box;margin:0;padding:0}
html,body{width:1200px;height:2695px;overflow:hidden}
body{position:relative;background:#fbfbfb;font-family:"Open Sans",Arial,sans-serif;color:var(--text);font-size:12px}
.abs{position:absolute}
a{color:inherit;text-decoration:none}

/* top bar */
.topbar{left:0;top:0;width:1200px;height:50px;background:#ececec}
.topbar .phone{left:50px;top:11px;font:700 22px "Open Sans",sans-serif;color:var(--ink);display:flex;align-items:center;gap:12px}
.topbar .hours{left:250px;top:17px;font-size:12px;color:#555}
.topbar .links{left:768px;top:18px;font-size:11px;color:#333;display:flex;gap:8px}
.topbar .links .login{color:var(--orange)}
.topbar .checkout{left:1047px;top:0;width:106px;height:50px;background:var(--orange);color:#fff;font-size:11px;font-weight:600;display:flex;align-items:center;justify-content:center;gap:6px}

/* header */
.header{left:0;top:50px;width:1200px;height:110px;background:#fff}
.brand{left:48px;top:32px;display:flex;align-items:center;gap:10px;font:600 30px "Raleway",sans-serif;color:var(--ink)}
.brand .mark{width:26px;height:26px;border-radius:50%;background:var(--orange)}
.search{left:462px;top:38px;width:441px;height:32px;border:1px solid var(--line);display:flex}
.search span{flex:1;padding:8px 12px;font-size:10px;color:#aaa}
.search b{width:75px;background:#333;color:#fff;font-size:10px;font-weight:600;display:flex;align-items:center;justify-content:center}
.cart{left:988px;top:38px;width:163px;height:32px;border:1px solid var(--line);font-size:10px;color:#888;display:flex;align-items:center;gap:8px;padding-left:10px}
.cart em{font-style:normal;color:var(--orange);font-weight:600}

/* nav */
.nav{left:0;top:160px;width:1200px;height:52px;background:var(--black)}
.nav ul{list-style:none;display:flex;height:52px;margin-left:55px}
.nav li{display:flex;align-items:center;padding:0 16px;color:#fff;font-size:11px;font-weight:600;border-right:1px solid #2a2a2a}
.nav li.home{padding:0 22px}

/* hero */
.hero{left:0;top:212px;width:1200px;height:498px;background:var(--hero)}
.hero h1{left:55px;top:58px;width:540px;font:400 84px/86px "Oswald",sans-serif;color:#3a3a3a;letter-spacing:-1px;white-space:nowrap}
.hero h1 .offer{color:var(--orange);letter-spacing:-3px}
.hero h1 .pct{font-size:.62em;letter-spacing:0}
.hero .sub{left:56px;top:252px;font-size:19px;color:#333}
.hero .sub a{color:var(--orange)}
.hero .lead{left:56px;top:290px;width:490px;font-size:12.5px;line-height:21px;color:#888}
.hero .btn{left:56px;top:348px;width:150px;height:40px;background:var(--orange);color:#fff;font-size:13px;font-weight:600;display:flex;align-items:center;justify-content:center}
.tv-main{left:607px;top:45px;width:381px;height:400px;border-radius:4px;background:linear-gradient(135deg,#1a3a12,#2f7a2a 45%,#1b4fb0 70%,#0e2a16);border:12px solid #1c1c1c}
.tv-side{left:1018px;top:105px;width:58px;height:330px;background:linear-gradient(90deg,#222,#777 50%,#333)}
.dots{left:1068px;top:450px;display:flex;gap:8px}
.dots i{width:14px;height:14px;border-radius:50%;border:2px solid var(--orange)}
.dots i.on{background:var(--orange)}
.hero-shadow{left:150px;top:705px;width:900px;height:22px;background:radial-gradient(ellipse at top,rgba(0,0,0,.22),transparent 70%)}

/* features */
.feature{top:763px;height:101px;background:linear-gradient(#fff,#e9e9e9);border:1px solid var(--line)}
.feature .icon{left:20px;top:20px;width:60px;height:60px;border-radius:50%;background:#fff;border:1px solid #ddd;display:flex;align-items:center;justify-content:center}
.feature .t{right:20px;top:28px;text-align:right}
.feature h3{font:500 20px "Raleway",sans-serif;color:var(--orange)}
.feature p{font-size:12px;color:#666;margin-top:4px}

/* side panels */
.side{left:57px;width:264px;background:var(--panel);border:1px solid #eee}
.side h4{height:50px;background:linear-gradient(#3a3a3a,#050505);color:#fff;font-size:12px;font-weight:600;padding:18px 26px}
.news-item{margin:0 18px 0 26px;padding:18px 0 14px;border-bottom:1px solid #ddd}
.news-item h5{font-size:11.5px;font-weight:700;color:#111}
.news-item p{font-size:11px;line-height:16px;color:#555;margin-top:6px}
.news-item.active p{color:var(--orange)}
.more{display:block;text-align:right;padding:16px 26px 0 0;font-size:10px;color:var(--orange)}
.blog-item{display:flex;gap:16px;margin:0 18px 0 22px;padding:18px 0 12px}
.blog-item .avatar{width:60px;height:52px;background:linear-gradient(#c9a585,#7a5b45);flex:none}
.blog-item p{font-size:11px;line-height:16px;color:#555}
.blog-item small{display:flex;justify-content:space-between;font-size:9px;color:#888;margin-top:4px}
.share{display:flex;gap:3px}
.share i{width:12px;height:12px;background:#1c5878}
.blog-more{display:block;text-align:right;padding:0 26px;font-size:10px;color:#2a86c8}

/* section titles */
.section-title{font:500 23px "Raleway",sans-serif;color:#222}
.section-title span{color:var(--orange)}
.sortby{left:1058px;top:920px;width:86px;height:30px;border:1px solid #ddd;background:#fff;font-size:9px;color:#555;display:flex;align-items:center;justify-content:center;gap:8px}

/* product cards */
.pcard{width:385px;height:201px;background:#fff;border:1px solid var(--line)}
.pcard.hot{background:var(--orange);border-color:var(--orange)}
.pcard .img{left:22px;top:30px;width:150px;height:130px;background:linear-gradient(#2d4a5a,#6a7f6a 60%,#222)}
.pcard .body{left:200px;top:30px;width:165px}
.pcard h3{font:400 19px "Open Sans",sans-serif;color:#222}
.pcard p{font-size:11px;line-height:16px;color:#777;margin-top:8px}
.pcard .rm{display:inline-block;margin-top:14px;border:1px solid var(--orange);color:var(--orange);font-size:9px;padding:6px 16px;background:#fff}
.pcard.hot h3,.pcard.hot p{color:#fff}

/* feature products */
.fcard{top:1527px;width:254px;height:386px;background:#fff;border:1px solid var(--line);text-align:center;overflow:hidden}
.fcard.sel{background:var(--orange-soft)}
.fcard .badge{left:18px;top:0;background:var(--red);color:#fff;font-size:8px;font-weight:700;padding:3px 6px}
.fcard .ribbon{right:-30px;top:12px;width:110px;transform:rotate(45deg);background:var(--orange);color:#fff;font-size:9px;font-weight:700;padding:3px 0}
.fcard .img{left:32px;top:45px;width:190px;height:130px;background:linear-gradient(#c23868,#6b2a5a 50%,#1a1a1a)}
.fcard .qv{left:58px;top:80px;width:140px;height:40px;background:rgba(40,40,40,.85);color:#fff;font-size:11px;font-weight:600;display:flex;align-items:center;justify-content:center;gap:14px}
.fcard h3{position:absolute;top:218px;width:100%;font-size:12px;font-weight:700;color:#222}
.fcard.sel h3{color:var(--orange)}
.fcard p{position:absolute;top:238px;left:20px;right:20px;font-size:10px;line-height:14px;color:#777}
.fcard .price{position:absolute;top:278px;left:16px;right:16px;display:flex;align-items:center;gap:10px;justify-content:center}
.price s{font-size:11px;color:#999}
.price b{font-size:21px;font-weight:400;color:var(--orange)}
.stars{color:#b8860b;font-size:14px;letter-spacing:-1px}
.stars i{color:#ccc;font-style:normal}
.actions{position:absolute;top:325px;left:14px;right:14px;display:flex;justify-content:space-between}
.actions span{width:40px;height:40px;border-radius:50%;border:1px solid #ccc;display:flex;align-items:center;justify-content:center;background:#fff}
.actions span.go{background:var(--orange);border-color:var(--orange)}

/* newsletter */
.newsletter{left:0;top:1949px;width:1200px;height:174px;background:var(--orange)}
.newsletter h2{left:178px;top:40px;font:300 34px "Raleway",sans-serif;color:#fff}
.newsletter p{left:90px;top:92px;width:390px;text-align:right;font-size:11px;line-height:16px;color:#fff}
.newsletter .email{left:515px;top:43px;width:248px;height:39px;background:#fff;font-size:10px;color:#999;padding:13px 22px}
.newsletter .sub{left:515px;top:97px;width:248px;height:39px;background:#2b2b2b;color:#fff;font-size:11px;font-weight:600;display:flex;align-items:center;justify-content:center}
.freeship{left:842px;top:25px;width:275px;height:124px;background:#2b2b2b;color:#fff}
.freeship h3{left:86px;top:18px;font:700 32px/33px "Open Sans",sans-serif}
.freeship small{left:94px;top:92px;font-size:12px}

/* follow */
.follow h2{left:0;top:2163px;width:1200px;text-align:center;font:500 23px "Raleway",sans-serif;color:var(--orange)}
.social{top:2225px;width:214px;height:51px;color:#fff;font:700 20px "Open Sans",sans-serif;display:flex;align-items:center;justify-content:center;gap:12px}
.social i{width:12px;height:12px;border-radius:50%;background:#fff}
.social-count{top:2288px;width:214px;text-align:center;font-size:12px;color:#888}

/* footer */
.footer{left:0;top:2340px;width:1200px;height:279px;background:var(--black);color:#bbb}
.fcol{top:68px}
.fcol h4{font-size:12px;font-weight:600;color:#fff;margin-bottom:30px}
.fcol li{list-style:none;font-size:10px;line-height:22.5px;color:#999}
.fcol .contact li{display:flex;gap:12px;align-items:flex-start;line-height:18px}
.bottom{left:0;top:2619px;width:1200px;height:76px;background:#050505;color:#bbb;font-size:10px}
.bottom p{left:52px;top:26px}
.cards{right:50px;top:20px;display:flex;gap:7px}
.cards i{width:44px;height:30px;border-radius:4px;background:#f3f3f3}
</style>
</head>
<body>

<div class="abs topbar">
  <div class="abs phone">
    <svg width="20" height="20" viewBox="0 0 24 24"><path fill="#e38a17" d="M6.6 10.8a15 15 0 0 0 6.6 6.6l2.2-2.2c.3-.3.7-.4 1-.2 1.1.4 2.3.6 3.6.6.6 0 1 .4 1 1V20c0 .6-.4 1-1 1A17 17 0 0 1 3 4c0-.6.4-1 1-1h3.5c.6 0 1 .4 1 1 0 1.3.2 2.5.6 3.6.1.3 0 .7-.2 1z"/></svg>
    01632 960418
  </div>
  <div class="abs hours">Monday - Friday 9am - 5pm</div>
  <div class="abs links"><a class="login">LOGIN/REGISTER</a><span>|</span><a>MY ACCOUNT</a><span>|</span><a>WISHLIST - 0</a></div>
  <a class="abs checkout">CHECKOUT <svg width="14" height="12" viewBox="0 0 14 12"><path fill="#fff" d="M0 4h8V0l6 6-6 6V8H0z"/></svg></a>
</div>

<header class="abs header">
  <div class="abs brand"><span class="mark"></span>Brook Lantern</div>
  <div class="abs search"><span>Enter keyword</span><b>SEARCH</b></div>
  <div class="abs cart">
    <svg width="16" height="14" viewBox="0 0 16 14"><path fill="#e38a17" d="M0 0h3l.6 2H16l-2 6H5l.5 2H14v1.5H4.3L1.9 1.5H0z"/><circle cx="6" cy="13" r="1" fill="#e38a17"/><circle cx="13" cy="13" r="1" fill="#e38a17"/></svg>
    <em>CART :</em> 0 (Items) <span style="margin-left:22px">▾</span>
  </div>
</header>

<nav class="abs nav">
  <ul>
    <li class="home"><svg width="20" height="18" viewBox="0 0 20 18"><path fill="#e38a17" d="M10 0l10 9h-3v9h-5v-6H8v6H3V9H0z"/></svg></li>
    <li>ABOUT</li><li>PRODUCTS</li><li>ABOUT LUMEN</li><li>WEBSITE DESIGN</li><li>NEWS</li><li>SAMPLE MODEL</li><li>NEW MODEL</li><li>TESTIMONIALS</li><li>BLOG</li><li>CONTACT US</li>
  </ul>
</nav>

<section class="abs hero">
  <h1 class="abs">LATEST MODEL<br>LED TV <span class="offer">25<span class="pct">%</span> OFFER</span></h1>
  <p class="abs sub">Many model available, <a>click here</a> for more details</p>
  <p class="abs lead">Lorem ipsum dolor sit amet, consectetur adipiscing elit, sed do eiusmod tempor incididunt ut labore et dolore magna aliqua.</p>
  <a class="abs btn">SHOP NOW</a>
  <div class="abs tv-main" role="img" aria-label="Flat-screen LED television showing a colourful flower and hummingbird"></div>
  <div class="abs tv-side" role="img" aria-label="Side view of a slim LED television on its stand"></div>
  <div class="abs dots"><i class="on"></i><i></i><i></i><i></i></div>
</section>
<div class="abs hero-shadow"></div>

<div class="abs feature" style="left:50px;width:263px">
  <div class="abs icon"><svg width="28" height="28" viewBox="0 0 24 24"><path fill="none" stroke="#e38a17" stroke-width="2" d="M7 10v11H3V10zM7 10l4-8c2 0 2 2 2 3v3h6a2 2 0 0 1 2 2l-2 9H7"/></svg></div>
  <div class="abs t"><h3>SATISFACTION</h3><p>100% Guaranteed</p></div>
</div>
<div class="abs feature" style="left:332px;width:259px">
  <div class="abs icon"><svg width="30" height="22" viewBox="0 0 30 22"><path fill="#e38a17" d="M0 0h18v16H0zM19 5h6l5 6v5H19z"/><circle cx="6" cy="18" r="3.5" fill="#e38a17" stroke="#fff"/><circle cx="24" cy="18" r="3.5" fill="#e38a17" stroke="#fff"/></svg></div>
  <div class="abs t"><h3>FREE SHIPPING</h3><p>on orders over $99</p></div>
</div>
<div class="abs feature" style="left:614px;width:261px">
  <div class="abs icon"><svg width="28" height="28" viewBox="0 0 24 24"><path fill="none" stroke="#e38a17" stroke-width="3" d="M4 11a8 8 0 0 1 14-5M20 13a8 8 0 0 1-14 5"/><path fill="#e38a17" d="M20 2v7h-7zM4 22v-7h7z"/></svg></div>
  <div class="abs t"><h3>7 DAY</h3><p>Easy to Return items</p></div>
</div>
<div class="abs feature" style="left:893px;width:258px">
  <div class="abs icon"><svg width="30" height="30" viewBox="0 0 24 24"><circle cx="12" cy="12" r="10" fill="none" stroke="#e38a17" stroke-width="2"/><circle cx="12" cy="12" r="4" fill="none" stroke="#e38a17" stroke-width="2"/><path stroke="#e38a17" stroke-width="2" d="M5 5l4 4M19 5l-4 4M5 19l4-4M19 19l-4-4"/></svg></div>
  <div class="abs t"><h3>SUPPORT</h3><p>Customer Service</p></div>
</div>

<aside class="abs side" style="top:934px;height:467px">
  <h4>LATEST NEWS</h4>
  <div class="news-item active"><h5>LOREM IPSUM DOLOR SIT AMET</h5><p>We have just completed a foamex cut out for a birthday party.</p></div>
  <div class="news-item"><h5>LOREM IPSUM DOLOR SIT AMET</h5><p>We have just completed a foamex cut out for a birthday party.</p></div>
  <div class="news-item"><h5>LOREM IPSUM DOLOR SIT AMET</h5><p>We have just completed a foamex cut out for a birthday party.</p></div>
  <div class="news-item" style="border:0"><h5>LOREM IPSUM DOLOR SIT AMET</h5><p>We have just completed a foamex cut out for a birthday party.</p></div>
  <a class="more" style="padding-top:4px">More News</a>
</aside>

<h2 class="abs section-title" style="left:354px;top:925px"><span>NEW</span> PRODUCTS</h2>
<div class="abs sortby">SORT BY <span>▾</span></div>

<article class="abs pcard hot" style="left:354px;top:979px">
  <div class="abs img" role="img" aria-label="LED television showing a lakeside landscape"></div>
  <div class="abs body"><h3>LATEST LED TV</h3><p>Lorem ipsum dolor sit amet, consectetur adipiscing elit, sed do eiusmod tempor</p><a class="rm">READ MORE</a></div>
</article>
<article class="abs pcard" style="left:765px;top:979px">
  <div class="abs img" role="img" aria-label="Satellite television showing a menu screen" style="background:linear-gradient(#1a1a1a,#5a4a3a 50%,#111)"></div>
  <div class="abs body"><h3>Lumen Satellite TV</h3><p>Lorem ipsum dolor sit amet, consectetur adipiscing elit, sed do eiusmod tempor</p><a class="rm">READ MORE</a></div>
</article>
<article class="abs pcard" style="left:354px;top:1200px">
  <div class="abs img" role="img" aria-label="Television showing a green tree on a meadow" style="background:linear-gradient(#9fd0f0,#6cb84a 60%,#3a7a2a)"></div>
  <div class="abs body"><h3>12-Volt TV's</h3><p>Lorem ipsum dolor sit amet, consectetur adipiscing elit, sed do eiusmod tempor</p><a class="rm">READ MORE</a></div>
</article>
<article class="abs pcard" style="left:765px;top:1200px">
  <div class="abs img" role="img" aria-label="Television showing a dark green garden scene" style="background:linear-gradient(#0e2a12,#3a7a2a 55%,#0a1a0a)"></div>
  <div class="abs body"><h3>PVR TV's</h3><p>Lorem ipsum dolor sit amet, consectetur adipiscing elit, sed do eiusmod tempor</p><a class="rm">READ MORE</a></div>
</article>

<aside class="abs side" style="top:1464px;height:436px">
  <h4>LATEST BLOG</h4>
  <div class="blog-item"><div class="avatar" role="img" aria-label="Author portrait"></div><div><p>We have just completed a foamex cut out for a birthday party.</p><small>Posted by : 08 Aug 2015 <span class="share"><i></i><i style="background:#1da3e2"></i><i style="background:#1e74d0"></i></span></small></div></div>
  <div class="blog-item"><div class="avatar" role="img" aria-label="Author portrait"></div><div><p>We have just completed a foamex cut out for a birthday party.</p><small>Posted by : 08 Aug 2015 <span class="share"><i></i><i style="background:#1da3e2"></i><i style="background:#1e74d0"></i></span></small></div></div>
  <div class="blog-item"><div class="avatar" role="img" aria-label="Author portrait"></div><div><p>We have just completed a foamex cut out for a birthday party.</p><small>Posted by : 08 Aug 2015 <span class="share"><i></i><i style="background:#1da3e2"></i><i style="background:#1e74d0"></i></span></small></div></div>
  <a class="blog-more" style="margin-top:16px">Read More Blogs</a>
</aside>

<h2 class="abs section-title" style="left:359px;top:1458px"><span>FEATURE</span> PRODUCT</h2>

<article class="abs fcard" style="left:357px">
  <span class="abs badge">25%</span><span class="abs ribbon">NEW</span>
  <div class="abs img" role="img" aria-label="Television showing a butterfly on a red flower"></div>
  <h3>NAME OF THE PRODUCT</h3>
  <p>Lorem ipsum dolor sit amet, consectetur adipi-scing elit, sed do eiusmod tempor</p>
  <div class="price"><s>$35.00</s><b>$ 29.00</b><span class="stars">★★<i>★★★</i></span></div>
  <div class="actions">
    <span><svg width="16" height="14" viewBox="0 0 16 14"><path fill="#999" d="M0 0h3l.6 2H16l-2 6H5l.5 2H14v1.5H4.3L1.9 1.5H0z"/></svg></span>
    <span><svg width="16" height="14" viewBox="0 0 16 14"><path fill="none" stroke="#999" stroke-width="1.5" d="M8 13S1 8.5 1 4.5A3.3 3.3 0 0 1 8 3a3.3 3.3 0 0 1 7 1.5C15 8.5 8 13 8 13z"/></svg></span>
    <span><svg width="14" height="14" viewBox="0 0 14 14"><path stroke="#999" stroke-width="1.5" d="M2 12l10-10M8 2h4v4M6 12H2V8"/></svg></span>
    <span><svg width="16" height="16" viewBox="0 0 16 16"><rect x="1" y="1" width="13" height="13" fill="none" stroke="#999" stroke-width="1.5"/><path fill="none" stroke="#999" stroke-width="1.8" d="M4 8l3 3 7-8"/></svg></span>
  </div>
</article>
<article class="abs fcard sel" style="left:627px">
  <span class="abs badge">25%</span>
  <div class="abs img" role="img" aria-label="Hand holding a tablet device" style="background:linear-gradient(#f6dfbd,#e9c9a0)"></div>
  <div class="abs qv">QUICK VIEW <span>›</span></div>
  <h3>NAME OF THE PRODUCT</h3>
  <p>Lorem ipsum dolor sit amet, consectetur adipi-scing elit, sed do eiusmod tempor</p>
  <div class="price"><s>$35.00</s><b>$ 29.00</b><span class="stars">★★<i>★★★</i></span></div>
  <div class="actions">
    <span class="go"><svg width="16" height="14" viewBox="0 0 16 14"><path fill="#fff" d="M0 0h3l.6 2H16l-2 6H5l.5 2H14v1.5H4.3L1.9 1.5H0z"/></svg></span>
    <span><svg width="16" height="14" viewBox="0 0 16 14"><path fill="none" stroke="#999" stroke-width="1.5" d="M8 13S1 8.5 1 4.5A3.3 3.3 0 0 1 8 3a3.3 3.3 0 0 1 7 1.5C15 8.5 8 13 8 13z"/></svg></span>
    <span><svg width="14" height="14" viewBox="0 0 14 14"><path stroke="#999" stroke-width="1.5" d="M2 12l10-10M8 2h4v4M6 12H2V8"/></svg></span>
    <span><svg width="16" height="16" viewBox="0 0 16 16"><rect x="1" y="1" width="13" height="13" fill="none" stroke="#999" stroke-width="1.5"/><path fill="none" stroke="#999" stroke-width="1.8" d="M4 8l3 3 7-8"/></svg></span>
  </div>
</article>
<article class="abs fcard" style="left:896px">
  <div class="abs img" role="img" aria-label="Television showing a tropical beach" style="background:linear-gradient(#7cc4ea,#2a8ab0 60%,#7a1a1a)"></div>
  <h3>NAME OF THE PRODUCT</h3>
  <p>Lorem ipsum dolor sit amet, consectetur adipi-scing elit, sed do eiusmod tempor</p>
  <div class="price"><s>$35.00</s><b>$ 29.00</b><span class="stars">★★<i>★★★</i></span></div>
  <div class="actions">
    <span><svg width="16" height="14" viewBox="0 0 16 14"><path fill="#999" d="M0 0h3l.6 2H16l-2 6H5l.5 2H14v1.5H4.3L1.9 1.5H0z"/></svg></span>
    <span><svg width="16" height="14" viewBox="0 0 16 14"><path fill="none" stroke="#999" stroke-width="1.5" d="M8 13S1 8.5 1 4.5A3.3 3.3 0 0 1 8 3a3.3 3.3 0 0 1 7 1.5C15 8.5 8 13 8 13z"/></svg></span>
    <span><svg width="14" height="14" viewBox="0 0 14 14"><path stroke="#999" stroke-width="1.5" d="M2 12l10-10M8 2h4v4M6 12H2V8"/></svg></span>
    <span><svg width="16" height="16" viewBox="0 0 16 16"><rect x="1" y="1" width="13" height="13" fill="none" stroke="#999" stroke-width="1.5"/><path fill="none" stroke="#999" stroke-width="1.8" d="M4 8l3 3 7-8"/></svg></span>
  </div>
</article>

<section class="abs newsletter">
  <h2 class="abs">Newsletter Sign Up</h2>
  <p class="abs">Lorem ipsum dolor sit amet conse ctetur adipiscing elit, sed do eiusmod tempor incididunt ut labore et dolore magna aliqua.</p>
  <div class="abs email">Enter your Email Address</div>
  <a class="abs sub">SUBSCRIBE</a>
  <div class="abs freeship">
    <svg class="abs" style="left:24px;top:48px" width="44" height="32" viewBox="0 0 30 22"><path fill="#fff" d="M0 0h18v16H0zM19 5h6l5 6v5H19z"/><circle cx="6" cy="18" r="3.5" fill="#fff" stroke="#2b2b2b"/><circle cx="24" cy="18" r="3.5" fill="#fff" stroke="#2b2b2b"/></svg>
    <h3 class="abs">FREE<br>SHIPPING</h3>
    <small class="abs">on order over $ 99</small>
  </div>
</section>

<section class="follow">
  <h2 class="abs">FOLLOW US TO STAY IN TOUCH</h2>
  <a class="abs social" style="left:226px;background:var(--fb)"><i></i>Facepage</a>
  <a class="abs social" style="left:508px;background:var(--tw)"><i></i>Chirper</a>
  <a class="abs social" style="left:792px;background:var(--li)"><i></i>Linkwork</a>
  <div class="abs social-count" style="left:226px">1234 Like</div>
  <div class="abs social-count" style="left:508px">1234 Followers</div>
  <div class="abs social-count" style="left:792px">1234 Connections</div>
</section>

<footer class="abs footer">
  <div class="abs fcol" style="left:54px"><h4>INFORMATION</h4><ul><li>ABOUT US</li><li>CUSTOMER SERVICE</li><li>PRIVACY POLICY</li><li>SEARCH TERMS</li><li>ORDERS AND RETURNS</li><li>CONTACT US</li></ul></div>
  <div class="abs fcol" style="left:325px"><h4>WHY BUY FROM US</h4><ul><li>SHIPPING &amp; RETURNS</li><li>SECURE SHOPPING</li><li>INTERNATIONAL SHIPPING</li><li>AFFILIATES</li><li>GROUP SALES</li></ul></div>
  <div class="abs fcol" style="left:625px"><h4>MY ACCOUNT</h4><ul><li>SIGN IN</li><li>VIEW CART</li><li>MY WISHLIST</li><li>TRACK MY ORDER</li><li>HELP</li></ul></div>
  <div class="abs fcol" style="left:869px"><h4>CONTACTS</h4>
    <ul class="contact">
      <li><svg width="10" height="14" viewBox="0 0 10 14"><path fill="#999" d="M5 0a5 5 0 0 1 5 5c0 4-5 9-5 9S0 9 0 5a5 5 0 0 1 5-5zm0 3a2 2 0 1 0 0 4 2 2 0 0 0 0-4z"/></svg><span>12 HARBOUR LANE, KELSO TD5 7QX<br>P. O BOX 40817, SCOTLAND</span></li>
      <li style="margin-top:14px"><svg width="12" height="12" viewBox="0 0 24 24"><path fill="#999" d="M6.6 10.8a15 15 0 0 0 6.6 6.6l2.2-2.2c.3-.3.7-.4 1-.2 1.1.4 2.3.6 3.6.6.6 0 1 .4 1 1V20c0 .6-.4 1-1 1A17 17 0 0 1 3 4c0-.6.4-1 1-1h3.5c.6 0 1 .4 1 1 0 1.3.2 2.5.6 3.6.1.3 0 .7-.2 1z"/></svg><span>CALL US: (800) 555-0142</span></li>
      <li style="margin-top:4px"><svg width="12" height="10" viewBox="0 0 12 10"><path fill="#999" d="M0 0h12v10H0z"/><path fill="none" stroke="#0c0c0c" d="M0 0l6 5 6-5"/></svg><span>EMAIL INFO@BROOK-LANTERN.NET</span></li>
    </ul>
  </div>
</footer>

<div class="abs bottom">
  <p class="abs">All Rights Reserved. Copyrights @ 2016</p>
  <div class="abs cards"><i></i><i></i><i></i><i></i></div>
</div>

</body>
</html>
```